I need a sophisticated and powerful book cover design that combines Japanese minimalism with contemporary appeal. The cover should convey personal transformation through the metaphor of a katana (Japanese sword).
Key Design Elements:
A katana, either partially shown or artistically rendered
Subtle Japanese design elements without being stereotypical
Clean, minimalist aesthetic
Professional font selection that bridges Eastern and Western typography
Color scheme: Deep blacks, steel grays, and possibly a touch of red or gold for accent
Mood/Style:
Professional and sophisticated
Blend of traditional Japanese aesthetics with modern design
Should appeal to personal development and business readers
Must convey strength and transformation
Elegant rather than aggressive
Specific Requirements:
Title: "The Lantern Compass"
Subtitle: "Quiet Practices for Growing Inner Steadiness and Calm Endurance Daily"
Author names: Moheshan Tadeli and Veena Tadeli
Cover dimensions: Standard hardcover book size (6" x 9")
Must work well in both physical and digital thumbnail formats
Should be striking and legible when viewed as a small image online
Design Specifics:
Japanese elements such as brushstroke effects, kanji characters, or wave patterns
The design should reflect the book's core message: personal transformation through Japanese wisdom principles, using the katana as a metaphor for growth and development.
Colors
Look and feel

```html
<!DOCTYPE html>
<html lang="en">
<head>
<meta charset="utf-8">
<title>The Lantern Compass — Book Cover</title>
<link rel="stylesheet" href="https://fonts.googleapis.com/css2?family=Fredoka:wght@600&family=Cabin:wght@500&family=Questrial&display=swap">
<style>
  :root {
    --surround: #04050b;
    --paper-top: #f3f8f3;
    --paper-mid: #e6eae8;
    --paper-low: #a7abb4;
    --paper-bottom: #787e8b;
    --sun-red: #ff0d12;
    --sun-fade: #f07a72;
    --blossom: #e04a78;
    --blossom-soft: #f2a9c0;
    --steel: #c9ccd1;
    --hilt: #141414;
    --ink: #111111;
    --title: #ffffff;
  }
  * { margin: 0; padding: 0; box-sizing: border-box; }
  html, body {
    width: 850px; height: 1200px; overflow: hidden;
    background: var(--surround);
  }
  .canvas { position: relative; width: 850px; height: 1200px; background: var(--surround); }
  .cover {
    position: absolute; left: 134px; top: 142px; width: 605px; height: 876px;
    overflow: hidden;
    background: linear-gradient(to bottom,
      var(--paper-top) 0%, var(--paper-top) 48%,
      var(--paper-mid) 62%, var(--paper-low) 85%, var(--paper-bottom) 100%);
  }
  .cover svg { position: absolute; left: 0; top: 0; }
  .title {
    position: absolute; left: 0; width: 100%; text-align: center;
    font-family: "Fredoka", "Arial Rounded MT Bold", sans-serif;
    font-weight: 600; color: var(--title); line-height: 1;
    letter-spacing: 0.5px;
  }
  .title-the { top: 285px; font-size: 36px; }
  .title-main { top: 324px; font-size: 76px; }
  .title-last { top: 406px; font-size: 54px; }
  .subtitle {
    position: absolute; left: 150px; width: 310px; top: 738px;
    text-align: center;
    font-family: "Cabin", "Gill Sans", sans-serif; font-weight: 500;
    font-size: 17px; line-height: 21px; color: var(--ink);
  }
  .authors {
    position: absolute; left: 0; width: 100%; top: 810px; text-align: center;
    font-family: "Questrial", "Century Gothic", sans-serif;
    font-size: 19px; color: var(--ink); letter-spacing: 0.3px;
  }
</style>
</head>
<body>
<div class="canvas">
  <div class="cover">
    <svg width="605" height="876" viewBox="0 0 605 876">
      <defs>
        <linearGradient id="sun-gradient" x1="0" y1="0" x2="0" y2="1">
          <stop offset="0" stop-color="var(--sun-red)"/>
          <stop offset="0.6" stop-color="var(--sun-red)"/>
          <stop offset="1" stop-color="var(--sun-fade)"/>
        </linearGradient>
        <radialGradient id="blossom-gradient" cx="0.55" cy="0.5" r="0.6">
          <stop offset="0" stop-color="var(--blossom)" stop-opacity="0.55"/>
          <stop offset="0.7" stop-color="var(--blossom-soft)" stop-opacity="0.35"/>
          <stop offset="1" stop-color="var(--blossom-soft)" stop-opacity="0"/>
        </radialGradient>
        <linearGradient id="sword-gradient" x1="0" y1="0" x2="0" y2="1">
          <stop offset="0" stop-color="var(--hilt)"/>
          <stop offset="0.3" stop-color="var(--hilt)"/>
          <stop offset="0.32" stop-color="var(--steel)"/>
          <stop offset="1" stop-color="var(--steel)"/>
        </linearGradient>
      </defs>
      <circle class="rising-sun" cx="303" cy="381" r="199" fill="url(#sun-gradient)"/>
      <rect class="blossom-branch" role="img" aria-label="Illustration of a flowering cherry blossom branch sweeping across the cover"
            x="39" y="224" width="566" height="591" rx="280" fill="url(#blossom-gradient)"/>
      <rect class="katana" role="img" aria-label="Illustration of a vertical katana with black and red wrapped hilt"
            x="270" y="44" width="52" height="693" rx="6" fill="url(#sword-gradient)" opacity="0.85"/>
    </svg>
    <div class="title title-the">THE</div>
    <div class="title title-main">LANTERN</div>
    <div class="title title-last">COMPASS</div>
    <p class="subtitle">Quiet Practices for Growing Inner Steadiness and Calm Endurance Daily</p>
    <p class="authors">MOHESHAN TADELI &amp; VEENA TADELI</p>
  </div>
</div>
</body>
</html>
```